'CALVENTO' NEW WINE LABEL DESIGN

I am looking for an exceptional and exciting design for a wine label called 'Calvento' meaning 'Lookout'. The design must feature the name 'Calvento', and the word 'Cabernet Sauvignon' in version 1 and 'Sauvignon Blanc' in version 2. It will also need the words 'Valle Central, Chile' at the bottom of the label as a prominent piece of information as well as the vintage 2017. Please produce the work in size 80mm x 100mm. Feel free to use colour in addition to black/white and ensue that the label is easy to read on a shelf placement.
Target Market(s)
SUPERMARKETS & WINE STORES
Requirements
Must have
- EASY TO READ, USE COLOURS LIKE GREEN FOR SAUVIGNON & RED FOR CABERNET SAUVIGNON
- FULL BOTTLE SHOT MUST BE IN PROVIDED DESIGNS. ALL BOTTLE TOPS SHOULD BE QUORLEX STYLE (SCREW TOP)
- PLEASE NOTE THAT LABEL INFORMATION MUSY BE EASY TO READ I.E. VINTAGE, PLACE OF ORGIN ALTHOUGH NOT THE MAIN CONTENT MUST STILL BE CLEAR.
Nice to have
- ARTISTIC REFERENCE LINK TO NAME & ANDES BUT NOT PICTURES OF MOUNTAINS
Should not have
- PICTURES OF GRAPES
- PICTURES OF VINEYARDS
- PICTURES OF MOUNTAINS

```html
<!DOCTYPE html>
<html lang="en">
<head>
<meta charset="utf-8">
<title>Calvento Wine Labels</title>
<link rel="stylesheet" href="https://fonts.googleapis.com/css2?family=Cormorant+Garamond:wght@500;700&family=Libre+Baskerville:wght@400;700&display=swap">
<style>
  :root {
    --canvas: #f1f1f1;
    --paper: #ffffff;
    --ink: #151515;
    --ink-soft: #2b2b2b;
    --sauvignon: #8a8b2c;
    --sauvignon-text: #7d7c33;
    --cabernet: #8e2b23;
    --cabernet-text: #8a2a26;
    --band-text: #f4f1e6;
  }
  * { margin: 0; padding: 0; box-sizing: border-box; }
  html, body {
    width: 1200px;
    height: 1200px;
    overflow: hidden;
    background: var(--canvas);
  }
  .label-sheet {
    width: 1200px;
    height: 1200px;
    display: flex;
    justify-content: center;
    align-items: center;
    gap: 64px;
  }
  .label {
    position: relative;
    width: 500px;
    height: 625px;
    background: var(--paper);
    box-shadow: 0 2px 10px rgba(0,0,0,0.12);
    overflow: hidden;
  }
  .label__brand {
    position: absolute;
    top: 30px;
    left: 0;
    right: 0;
    text-align: center;
    font-family: "Libre Baskerville", "Times New Roman", serif;
    font-weight: 700;
    font-size: 62px;
    letter-spacing: 1px;
    color: var(--ink);
    line-height: 1;
  }
  .label__variety {
    position: absolute;
    top: 104px;
    left: 0;
    right: 0;
    text-align: center;
    font-family: "Cormorant Garamond", "Times New Roman", serif;
    font-weight: 500;
    font-size: 27px;
    letter-spacing: 1px;
    line-height: 1;
  }
  .label--sauvignon .label__variety { color: var(--sauvignon-text); }
  .label--cabernet .label__variety { color: var(--cabernet-text); }
  .label__landscape {
    position: absolute;
    top: 205px;
    left: 0;
    width: 500px;
    height: 175px;
  }
  .label__origin {
    position: absolute;
    top: 525px;
    left: 0;
    right: 0;
    text-align: center;
    font-family: "Libre Baskerville", "Times New Roman", serif;
    font-size: 19px;
    color: var(--ink-soft);
  }
  .label__vintage-band {
    position: absolute;
    left: 0;
    right: 0;
    bottom: 0;
    height: 46px;
    display: flex;
    align-items: center;
    justify-content: center;
    font-family: "Libre Baskerville", "Times New Roman", serif;
    font-size: 22px;
    letter-spacing: 1px;
    color: var(--band-text);
  }
  .label--sauvignon .label__vintage-band { background: var(--sauvignon); }
  .label--cabernet .label__vintage-band { background: var(--cabernet); }
</style>
</head>
<body>
  <main class="label-sheet">
    <article class="label label--sauvignon">
      <h1 class="label__brand">CALVENTO</h1>
      <h2 class="label__variety">SAUVIGNON BLANC</h2>
      <svg class="label__landscape" viewBox="0 0 500 175" role="img" aria-label="Watercolour lookout landscape in olive, sand and dark brown washes">
        <defs>
          <linearGradient id="sauvignon-wash" x1="0" y1="0" x2="0" y2="1">
            <stop offset="0" stop-color="#ffffff" stop-opacity="0"/>
            <stop offset="0.3" stop-color="#e6dcae"/>
            <stop offset="0.55" stop-color="#b9ad6a"/>
            <stop offset="0.72" stop-color="#3b3528"/>
            <stop offset="0.85" stop-color="#cfc6b4"/>
            <stop offset="1" stop-color="#ffffff" stop-opacity="0"/>
          </linearGradient>
        </defs>
        <rect x="0" y="0" width="500" height="175" fill="url(#sauvignon-wash)"/>
      </svg>
      <p class="label__origin">Valle Central, Chile</p>
      <div class="label__vintage-band">2017</div>
    </article>

    <article class="label label--cabernet">
      <h1 class="label__brand">CALVENTO</h1>
      <h2 class="label__variety">CABERNET SAUVIGNON</h2>
      <svg class="label__landscape" viewBox="0 0 500 175" role="img" aria-label="Watercolour lookout landscape in rose, rust and dark brown washes">
        <defs>
          <linearGradient id="cabernet-wash" x1="0" y1="0" x2="0" y2="1">
            <stop offset="0" stop-color="#ffffff" stop-opacity="0"/>
            <stop offset="0.3" stop-color="#efc3bb"/>
            <stop offset="0.55" stop-color="#c7705f"/>
            <stop offset="0.72" stop-color="#3a2822"/>
            <stop offset="0.85" stop-color="#d3c2bd"/>
            <stop offset="1" stop-color="#ffffff" stop-opacity="0"/>
          </linearGradient>
        </defs>
        <rect x="0" y="0" width="500" height="175" fill="url(#cabernet-wash)"/>
      </svg>
      <p class="label__origin">Valle Central, Chile</p>
      <div class="label__vintage-band">2017</div>
    </article>
  </main>
</body>
</html>
```